Valbrina Soletti Winery 2023 Label

We are just about to bottle our very first Napa Valley Cabernet Sauvignon and need label ideas

Target Market(s)

Cab drinkers who like Napa California Cabs

Industry/Entity Type

Wine Making

Logo Text

Valbrina Soletti 2023 Napa Estate Grown Cabernet Sauvignon

Requirements
Must have
• Winery Name, year of vintage and Napa Estate Cab
Nice to have
• If using the initials V and S use gold letters on black or red background

```html
<!DOCTYPE html>
<html lang="en">
<head>
<meta charset="utf-8">
<title>Valbrina Soletti Winery – 2023 Cabernet Sauvignon Label</title>
<link rel="stylesheet" href="https://fonts.googleapis.com/css2?family=Great+Vibes&family=Cormorant+SC:wght@600;700&family=Poppins:wght@300&display=swap">
<style>
  :root {
    --page-bg: #f7f7f7;
    --label-black: #141210;
    --gold: #c9a24a;
    --gold-deep: #b48d3a;
    --note-ink: #4a4a4a;
  }
  * { margin: 0; padding: 0; box-sizing: border-box; }
  html, body {
    width: 1200px;
    height: 800px;
    overflow: hidden;
    background: var(--page-bg);
  }
  .canvas {
    position: relative;
    width: 1200px;
    height: 800px;
  }
  .wine-label {
    position: absolute;
    left: 460px;
    top: 120px;
    width: 280px;
    height: 420px;
    background: var(--label-black);
    color: var(--gold);
    text-align: center;
    display: flex;
    flex-direction: column;
    align-items: center;
  }
  .winery-name {
    font-family: "Great Vibes", cursive;
    font-weight: 400;
    font-size: 50px;
    line-height: 44px;
    margin-top: 24px;
    letter-spacing: 0.5px;
  }
  .winery-name span { display: block; }
  .crest-mark {
    margin-top: 14px;
    width: 150px;
    height: 120px;
    display: flex;
    align-items: center;
    justify-content: center;
    gap: 8px;
    font-family: "Cormorant SC", serif;
    font-weight: 700;
    font-size: 17px;
    letter-spacing: 1px;
    line-height: 1.1;
    color: var(--gold);
  }
  .crest-mark .mark-square {
    width: 12px;
    height: 12px;
    background: var(--gold-deep);
    flex: none;
  }
  .vintage-details {
    font-family: "Cormorant SC", serif;
    font-weight: 700;
    line-height: 1;
    margin-top: 8px;
  }
  .vintage-year { font-size: 25px; font-weight: 600; letter-spacing: 2px; }
  .region { font-size: 36px; letter-spacing: 2px; margin-top: 2px; }
  .estate { font-size: 24px; letter-spacing: 1px; margin-top: 3px; }
  .varietal { font-size: 32px; letter-spacing: 1.5px; margin-top: 4px; line-height: 0.92; }
  .presentation-note {
    position: absolute;
    left: 400px;
    top: 680px;
    width: 400px;
    margin-left: -0px;
    font-family: "Poppins", sans-serif;
    font-weight: 300;
    font-size: 14.5px;
    line-height: 20.5px;
    color: var(--note-ink);
    text-align: center;
    white-space: nowrap;
    display: flex;
    flex-direction: column;
    align-items: center;
  }
</style>
</head>
<body>
  <main class="canvas">
    <section class="wine-label" aria-label="Valbrina Soletti 2023 Napa Estate Grown Cabernet Sauvignon label">
      <h1 class="winery-name"><span>Valbrina</span><span>Soletti</span></h1>
      <div class="crest-mark">
        <span class="mark-square"></span>
        <span>Valbrina<br>Soletti</span>
      </div>
      <div class="vintage-details">
        <p class="vintage-year">2023</p>
        <p class="region">NAPA</p>
        <p class="estate">ESTATE GROWN</p>
        <p class="varietal">CABERNET<br>SAUVIGNON</p>
      </div>
    </section>
    <p class="presentation-note">
      <span>This presentation is just the first draft, main and initial idea.</span>
      <span>Any addition of colors, as requested by the briefing or the client's wishes,</span>
      <span>will be made after the first feedback, as well as future changes.</span>
    </p>
  </main>
</body>
</html>
```